quillmetric corporate presentation

We have a wireframe presentation with 18 slides to be implemented in Google slides (powerpoint optional although we would rather prefer Google slides). Please, be creative and don't take the examples in the wireframe as literal. We also provide the following:

- Color palet
- quillmetric Logos
- Slide wireframe
- slide reference for slide number 5.
- Flyer
- Partner logos

You can find all the materials here: https://files.plinthbox.example/share/7kqTr2mWx9LpBn4Zc

```html
<!DOCTYPE html>
<html lang="en">
<head>
<meta charset="utf-8">
<title>quillmetric corporate presentation</title>
<link href="https://fonts.googleapis.com/css2?family=Montserrat:wght@300;400;500;600;700&display=swap" rel="stylesheet">
<style>
:root{
  --backdrop-edge:#cbbcfb;
  --backdrop-core:#f4fbff;
  --plum:#7b0a7e;
  --teal:#0e9aa7;
  --teal-bright:#0aa39c;
  --orange:#fbab45;
  --navy:#0b3462;
  --blue:#1479d6;
  --ink:#1d1d1f;
  --panel-grey:#f2f2f2;
  --white:#ffffff;
}
*{margin:0;padding:0;box-sizing:border-box}
html,body{width:1200px;height:892px;overflow:hidden}
body{
  font-family:'Montserrat',sans-serif;
  background:radial-gradient(ellipse 60% 65% at 50% 75%,var(--backdrop-core) 0%,#dde6fc 45%,var(--backdrop-edge) 100%);
  position:relative;
}
.slide{
  position:absolute;width:480px;height:270px;background:var(--white);
  box-shadow:0 8px 18px rgba(60,40,120,.18);overflow:hidden;
}
.slide--cover{left:60px;top:107px;background:linear-gradient(120deg,#7a1585 0%,#4e4a8a 45%,#2f7896 75%,var(--teal-bright) 100%)}
.slide--about{left:660px;top:107px}
.slide--future{left:60px;top:448px}
.slide--services{left:660px;top:448px}

.brand{position:absolute;display:flex;align-items:center;gap:3px;font-weight:700;font-size:14px;letter-spacing:-.2px;color:var(--navy)}
.brand__mark{width:8px;height:8px;background:var(--teal)}
.brand--top{left:9px;top:9px;color:var(--white)}
.brand--corner{right:10px;bottom:10px}

.cover__title{position:absolute;left:0;right:0;top:90px;text-align:center;color:var(--white);font-weight:300;font-size:19.5px;line-height:25px;opacity:.92}
.cover__lead{position:absolute;left:0;right:0;top:157px;text-align:center;color:var(--white);font-weight:500;font-size:9.6px;line-height:11.5px}

.slide__heading{position:absolute;left:24px;top:16px;color:var(--plum);font-weight:700;font-size:16px}

.about__panel{
  position:absolute;left:22px;top:53px;width:435px;height:164px;
  background:radial-gradient(ellipse 55% 75% at 52% 45%,var(--blue) 0%,#0d5aa8 55%,var(--navy) 100%);
  clip-path:polygon(0 0,408px 0,100% 27px,100% 100%,27px 100%,0 137px);
  color:var(--white);text-align:center;
}
.about__title{position:absolute;left:0;right:0;top:34px;font-weight:300;font-size:19.5px}
.about__text{position:absolute;left:20px;right:20px;top:89px;font-size:9.6px;line-height:13px;opacity:.92}

.quote{position:absolute;left:20px;top:84px;width:170px;border-left:2px solid var(--plum);padding-left:14px;font-size:9.6px;line-height:13px;color:var(--ink)}
.quote__source{position:absolute;left:44px;top:186px;font-size:9.6px;font-weight:700;color:var(--ink)}
.quote__source::before{content:"-";font-weight:500;margin-right:14px}
.future__visual{
  position:absolute;left:224px;top:69px;width:236px;height:132px;
  background:radial-gradient(circle at 30% 45%,#ff4fb8 0%,#9b1a8f 22%,#3a1466 52%,#150b33 100%);
  clip-path:polygon(0 0,216px 0,100% 20px,100% 100%,20px 100%,0 112px);
}

.services__panel{position:absolute;left:17px;top:50px;width:445px;height:169px;background:var(--panel-grey)}
.tag{
  position:absolute;display:flex;align-items:center;justify-content:center;text-align:center;
  color:var(--white);font-weight:700;font-size:9.4px;line-height:11px;
  clip-path:polygon(0 0,calc(100% - 4px) 0,100% 4px,100% 100%,4px 100%,0 calc(100% - 4px));
}
.tag--teal{background:var(--teal);top:66px;width:76px;height:21px}
.tag--orange{background:var(--orange);top:66px;width:102px;height:37px}
.tag--agentic{left:18px}
.tag--agent{left:112px}
.tag--ml{left:205px}
.tag--viz{left:326px}
</style>
</head>
<body>

<section class="slide slide--cover">
  <div class="brand brand--top"><span class="brand__mark"></span>quillmetric</div>
  <h1 class="cover__title">Leading the future<br>with Data and Intelligence</h1>
  <p class="cover__lead">We are a premier Professional Services company specialized in the design and<br>implementation of cutting edge technologies in Cloud, Data Analytics &amp; AI</p>
</section>

<section class="slide slide--about">
  <h2 class="slide__heading">About us</h2>
  <div class="about__panel">
    <p class="about__title">Data analytics &amp; AI for nonconformists</p>
    <p class="about__text">We are a leading professional services company specialized in the design and implementation of cutting edge technologies in Cloud, Data&nbsp; analytics &amp; AI.</p>
  </div>
  <div class="brand brand--corner"><span class="brand__mark"></span>quillmetric</div>
</section>

<section class="slide slide--future">
  <h2 class="slide__heading">The future is now</h2>
  <blockquote class="quote">“Generative AI has the potential to add trillions of dollars in value to the global economy and accelerate productivity growth for individuals, businesses and the economy as a whole.”</blockquote>
  <p class="quote__source">Harwell &amp; Pryce</p>
  <div class="future__visual" role="img" aria-label="Photo of a person touching a glowing holographic interface in neon pink and purple light"></div>
  <div class="brand brand--corner"><span class="brand__mark"></span>quillmetric</div>
</section>

<section class="slide slide--services">
  <h2 class="slide__heading">What we do</h2>
  <div class="services__panel">
    <div class="tag tag--teal tag--agentic">Agentic AI</div>
    <div class="tag tag--teal tag--agent">AI Agent</div>
    <div class="tag tag--orange tag--ml">Advanced<br>Analytics &amp; ML</div>
    <div class="tag tag--orange tag--viz">Data Analytics &amp;<br>Visualization</div>
  </div>
  <div class="brand brand--corner"><span class="brand__mark"></span>quillmetric</div>
</section>

</body>
</html>
```